Prominent Trial Lawyer need a Brochure Design for his firm

Harold J. Brantley of The Brantley Law Firm has been successfully trying severe and complex for over 28 years. He holds the largest verdict in the history of South Georgia of $150,000,000.00 before the late Leonard P. Vasquez in the Okefen District of the Southern District of Georgia. He specializes in sever injuries, whether by auto accident, trucking accident or medical malpractice. He is also well know for his successful trial of business disputes and high net-worth Divorces.
Target Market(s)
Persons who need an aggressive, experienced trial lawyer especially for personal injury, but also for other civil and business matters, high end divorde
Industry/Entity Type
Medical
Contact Information for Business Card
Need to use coloring and logo uplaoded
Requirements
Must have
- 1) biography of principal, Harold J. Brantley
- 2) what we do
- 3) specific cases handled, with specific outcomes (will be supplied)

```html
<!DOCTYPE html>
<html lang="en">
<head>
<meta charset="utf-8">
<title>The Brantley Law Firm – Brochure</title>
<link href="https://fonts.googleapis.com/css2?family=Lato:ital,wght@0,300;0,400;0,700;1,300&display=swap" rel="stylesheet">
<style>
  :root {
    --brand-red: #d9161d;
    --brand-red-dark: #b70f15;
    --ink: #1d1d1d;
    --body-ink: #2b2b2b;
    --quote-ink: #555555;
    --paper: #f4f4f2;
    --paper-shade: #e6e6e3;
    --backdrop: #ffffff;
    --white: #ffffff;
  }
  * { box-sizing: border-box; margin: 0; padding: 0; }
  html, body { width: 1200px; height: 1000px; overflow: hidden; background: var(--backdrop); }
  body { font-family: "Lato", Arial, sans-serif; color: var(--body-ink); }

  .brochure {
    position: absolute; left: 45px; top: 95px;
    width: 1110px; height: 810px;
    display: flex;
    box-shadow: 0 6px 24px rgba(0,0,0,.18);
  }
  .panel { width: 370px; height: 100%; position: relative; }

  /* Cover */
  .panel--cover {
    background: linear-gradient(180deg, var(--paper) 0%, var(--paper-shade) 100%);
    display: flex; flex-direction: column; align-items: center;
    padding: 150px 30px 40px;
  }
  .cover__mark {
    width: 130px; height: 130px; border-radius: 50%;
    background: var(--brand-red);
  }
  .cover__name {
    margin-top: 48px; text-align: center;
    font-size: 38px; font-weight: 700; line-height: 1.15; color: var(--ink);
  }
  .cover__tagline {
    margin-top: 10px; font-size: 17px; letter-spacing: 1px; color: var(--brand-red);
  }
  .cover__quote {
    margin-top: auto; align-self: stretch;
    font-size: 17px; font-weight: 300; font-style: italic; line-height: 1.45; color: var(--quote-ink);
  }
  .cover__source { display: block; text-align: right; font-size: 12px; margin-top: 4px; }

  /* Inner red panel */
  .panel--firm {
    background: linear-gradient(160deg, var(--brand-red) 0%, var(--brand-red-dark) 100%);
    color: var(--white); padding: 32px 28px 24px;
  }
  .section-title {
    font-size: 17px; font-weight: 700; padding-bottom: 6px;
    border-bottom: 3px solid var(--white); width: 72%; margin-bottom: 14px;
  }
  .panel--firm p { font-size: 13px; line-height: 1.45; text-align: justify; }
  .team-photo {
    margin: 18px auto 22px; width: 228px; height: 150px; display: block;
    border: 3px solid var(--white);
  }
  .practice-intro { font-weight: 700; }
  .practice-list { list-style: none; margin-top: 10px; }
  .practice-list li { font-size: 13px; font-weight: 700; line-height: 1.5; padding-left: 10px; }
  .practice-list li::before { content: "- "; }

  /* Criminal defense panel */
  .panel--defense { background: var(--paper); padding: 32px 28px 24px; color: var(--body-ink); }
  .panel--defense .section-title { color: var(--ink); border-bottom-color: var(--brand-red); width: 80%; }
  .panel--defense p { font-size: 13px; line-height: 1.5; text-align: justify; margin-bottom: 12px; }
  .divider { height: 4px; width: 62%; background: var(--ink); margin: 24px auto; }
  .charge-list { list-style: none; margin-top: 10px; }
  .charge-list li { font-size: 13px; line-height: 1.75; padding-left: 26px; position: relative; }
  .charge-list li::before {
    content: ""; position: absolute; left: 6px; top: 7px;
    width: 9px; height: 9px; border-radius: 50%; background: var(--brand-red);
  }
</style>
</head>
<body>
  <div class="brochure">
    <section class="panel panel--cover">
      <div class="cover__mark"></div>
      <h1 class="cover__name">The Brantley<br>Law Firm</h1>
      <div class="cover__tagline">TRIAL LAWYER</div>
      <blockquote class="cover__quote">
        “Whether you are against Insurance Companies, Fortune 500 Companies or Goverments, we level the field and give you the edge.”
        <span class="cover__source">- The Brantley Law Firm</span>
      </blockquote>
    </section>

    <section class="panel panel--firm">
      <h2 class="section-title">Our Firm</h2>
      <p>Founded in 1989, the firm practices in business and general civil litigation, personal injury, real estate transaction and litigation, criminal defense, and family law. We love the practice of law and how it can help to resolve your civil and family disputes, to right the wrongs done by others, to protect your constitutional rights if you happened to be accused of a crime, to seek fair monetary compensation if you are entitled to. We at The Brantley Law Firm can ensure that you are best represented in courts utilizing the most up-to-date laws, diligent preparation and insightful understanding of your matter.</p>
      <svg class="team-photo" role="img" aria-label="Group photograph of the firm's attorneys" viewBox="0 0 228 150" preserveAspectRatio="none">
        <defs>
          <linearGradient id="photoTone" x1="0" y1="0" x2="1" y2="1">
            <stop offset="0" stop-color="#8a8580"/>
            <stop offset="1" stop-color="#2e3040"/>
          </linearGradient>
        </defs>
        <rect width="228" height="150" fill="url(#photoTone)"/>
      </svg>
      <h2 class="section-title">Our Practice Areas</h2>
      <p class="practice-intro">Listed below are The Brantley Law Firm’s areas of practice. The main titles link to their own page, which includes a general description of that area of practice.</p>
      <ul class="practice-list">
        <li>Personal Injury</li>
        <li>General Civil Litigation</li>
        <li>Real Estate Law</li>
        <li>Criminal Defense</li>
        <li>Business Transaction</li>
        <li>Insurance Coverage and Bad Faith Suits</li>
      </ul>
    </section>

    <section class="panel panel--defense">
      <h2 class="section-title">Criminal Defense</h2>
      <p>The Brantley Law Firm handles various criminal matters including but not limited to DUI, Assault and Battery, Prostitution, Theft, Forgery, Traffic Violations, Domestic Violence and Drug cases. We will do out utmost to achieve the best possible results. We will represent you for a jury trial as well to prove your innocence of the crime you are accused of. We promise to keep confidentiality when handling your sensitive criminal case and help you throughout this extremely stressful experience.</p>
      <p>If you, or a friend or family member, have been charged with a crime, an uncertain future lies ahead. It is important to have an attorney who knows what to expect in a criminal case, to explain the process, and to help make informed decisions about the best course of action.</p>
      <div class="divider"></div>
      <p>Our attorneys have represented clients who face all types of criminal charges, including:</p>
      <ul class="charge-list">
        <li>DUI</li>
        <li>Drug-related offenses</li>
        <li>Criminal Internet Offenses</li>
        <li>Traffic violations</li>
        <li>White collar crimes</li>
        <li>Felonies and Misdemeanors</li>
      </ul>
      <div class="divider"></div>
      <p>Our attorneys have extensive experience in trying criminal cases. We will not take any case we are not prepared to take to trial.</p>
    </section>
  </div>
</body>
</html>
```